letterhead design

can you create a letterhead using the logo you created and the following:

318 W Dunhaven Elgin IL 60123
(p) 847-555-0143
(f) 847-555-0178
www.thebrantleylawgroup.com

Industry/Entity Type

Law

Requirements
Must have
• Use logo attached: must have address 318 W Dunhaven Elgin IL 60123 phone 847-555-0143 fax 847-555-0178
Should not have
• Nothing other thank logo and address/phone/website

```html
<!DOCTYPE html>
<html lang="en">
<head>
<meta charset="utf-8">
<title>Brantley Law Group — Letterhead</title>
<link href="https://fonts.googleapis.com/css2?family=Poppins:wght@400;600&display=swap" rel="stylesheet">
<style>
  :root {
    --plum: #3d1526;
    --gold: #e2b45a;
    --paper: #ffffff;
  }
  html, body {
    margin: 0;
    padding: 0;
    width: 960px;
    height: 1200px;
    overflow: hidden;
    background: var(--paper);
  }
  .letterhead {
    position: relative;
    width: 960px;
    height: 1200px;
    background: var(--paper);
    font-family: "Poppins", sans-serif;
    color: var(--plum);
  }
  .brand {
    position: absolute;
    left: 80px;
    top: 100px;
    display: flex;
    align-items: center;
    gap: 12px;
    color: var(--gold);
    font-family: "Poppins", sans-serif;
    font-weight: 400;
    font-size: 22px;
    line-height: 1;
    letter-spacing: 0.5px;
    white-space: nowrap;
  }
  .brand-dot {
    width: 16px;
    height: 16px;
    border-radius: 50%;
    background: var(--gold);
  }
  .contact {
    position: absolute;
    left: 583px;
    top: 56px;
    margin: 0;
    padding: 0;
    list-style: none;
    font-size: 17px;
    letter-spacing: 0.4px;
  }
  .contact li {
    display: flex;
    align-items: center;
    height: 34.5px;
  }
  .contact svg {
    width: 15px;
    height: 15px;
    margin-right: 10px;
    fill: var(--plum);
  }
  .contact strong { font-weight: 600; }
  .edge-tab {
    position: absolute;
    right: 0;
    top: 47px;
    width: 18px;
    height: 150px;
    background: var(--gold);
  }
  .footer-band {
    position: absolute;
    left: 0;
    bottom: 0;
  }
</style>
</head>
<body>
<div class="letterhead">
  <header class="brand">
    <span class="brand-dot" aria-hidden="true"></span>
    <span class="brand-name">BRANTLEY LAW GROUP</span>
  </header>

  <ul class="contact">
    <li>318 W Dunhaven Elgin, IL 60123</li>
    <li>
      <svg viewBox="0 0 16 16" aria-label="Phone"><path d="M1 6c0-2 3-3 7-3s7 1 7 3v1h-4V5.5H5V7H1zM3 8h10l1 6H2zm5 1.5a2 2 0 1 0 0 4 2 2 0 0 0 0-4z"/></svg>
      847-555-0143
    </li>
    <li>
      <svg viewBox="0 0 16 16" aria-label="Fax"><path d="M4 1h8v4H4zM1 6h14v7h-3v2H4v-2H1zm4 5v3h6v-3zm7-3.5a1 1 0 1 0 0 2 1 1 0 0 0 0-2z"/></svg>
      847-555-0178
    </li>
    <li>www.<strong>thebrantleylawgroup</strong>.com</li>
  </ul>

  <div class="edge-tab" aria-hidden="true"></div>

  <svg class="footer-band" width="960" height="27" aria-hidden="true">
    <polygon points="0,0 551,0 529,27 0,27" fill="var(--plum)"/>
    <polygon points="564,0 960,0 960,27 544,27" fill="var(--gold)"/>
  </svg>
</div>
</body>
</html>
```